Modern business card for triathlon training business in Australia

We need a business card design for our triathlon training company.

Pace with Us Fitness is an Australian business, owned by women, run for women. Pace with Us Fitness helps women prepare or improve triathlon skills and confidence through triathlon camps completely designed for women.

Our camps focus on preparing women both physically and mentally for their next (or first!) triathlon.

You can see our website www.pacewithusfitness.com.au for more info about our business and our style.

We've attached two of our logos and are happy to consider a design that utilised either colour scheme with the teal colour being our 'feature' colour. We don't want overly feminine cards but rather cards that are professional and neat. If the inclusion of any pictures/art is warranted, this should be focused on our swim/ride/run theme and in that specific order (swim/ride/run).

The business card needs to be a printable design and the contact details will need to change for our two employees.

Target Market(s)

Female clients and partners/vendors/sponsors that we work with in the triathlon industry

Industry/Entity Type

Fitness

Contact Information for Business Card

Pace with Us Fitness (business name)
Nina Carver
Business Director
Mobile: 0438 916 207
Email: nina@pacewithusfitness.com.au
www.pacewithusfitness.com.au

Second business card:
Pace with Us Fitness
Bel Stray
Coaching Director
Mobile: 0459 260 718
Email: bel@pacewithusfitness.com.au

Font styles to use
Serif
Sans Serif

Requirements
Must have
• Core contact details above, our logo and be a printable design
Should not have
• Pink
• Cursive/script fonts

```html
<!DOCTYPE html>
<html lang="en">
<head>
<meta charset="utf-8">
<title>Pace with Us Fitness – Business Card</title>
<link rel="stylesheet" href="https://fonts.googleapis.com/css2?family=Roboto+Condensed:wght@300;400;700&display=swap">
<style>
  :root {
    --teal: #1ea8c8;
    --teal-deep: #168aa6;
    --ring: #7fd0e3;
    --white: #ffffff;
    --ribbon-pale: #e6f4f8;
    --backdrop: #f3ecdf;
    --icon: #0d5a6e;
    --swim-tone: #3b6fa8;
    --ride-tone: #5f8d7a;
    --run-tone: #b6a36a;
  }
  * { margin: 0; padding: 0; box-sizing: border-box; }
  html, body { width: 1200px; height: 1000px; overflow: hidden; }
  body {
    background: var(--backdrop);
    font-family: "Roboto Condensed", Arial, sans-serif;
    display: flex; align-items: center; justify-content: center;
  }
  .card {
    position: relative;
    width: 900px; height: 550px;
    background: var(--teal);
    border-bottom: 10px solid var(--teal-deep);
    box-shadow: 0 18px 40px rgba(0,0,0,0.12);
    overflow: hidden;
  }
  .brand {
    position: absolute; left: 60px; top: 84px;
    width: 240px;
    display: flex; align-items: center; gap: 12px;
  }
  .brand-dot {
    flex: none;
    width: 40px; height: 40px; border-radius: 50%;
    background: var(--white);
  }
  .brand-name {
    color: var(--white); font-weight: 700; font-size: 28px;
    letter-spacing: 0.5px; text-transform: uppercase; line-height: 1.05;
  }
  .brand-name span { display: block; }
  .disciplines {
    position: absolute; right: 50px; top: 70px;
    display: flex; gap: 26px;
  }
  .discipline {
    width: 160px; height: 160px; border-radius: 50%;
    border: 7px solid var(--ring);
  }
  .discipline.swim { background: radial-gradient(circle at 45% 40%, #8fb6de, var(--swim-tone)); }
  .discipline.ride { background: radial-gradient(circle at 45% 40%, #b9cfc3, var(--ride-tone)); }
  .discipline.run  { background: radial-gradient(circle at 45% 40%, #e3dcb8, var(--run-tone)); }
  .ribbon {
    position: absolute; left: 0; top: 290px;
    width: 360px; height: 140px;
  }
  .ribbon svg { position: absolute; inset: 0; }
  .person-name {
    position: absolute; left: 62px; top: 24px;
    color: var(--teal); font-weight: 700; font-size: 46px; line-height: 1;
  }
  .person-role {
    position: absolute; left: 50px; top: 88px;
    color: var(--teal); font-weight: 300; font-size: 27px; line-height: 1;
  }
  .contact {
    position: absolute; right: 50px; top: 330px;
    list-style: none; text-align: right; color: var(--white);
  }
  .contact li {
    display: flex; align-items: center; justify-content: flex-end; gap: 14px;
    font-weight: 300;
  }
  .contact .phone { font-size: 40px; margin-bottom: 14px; }
  .contact .email, .contact .web { font-size: 25px; margin-bottom: 14px; }
  .contact svg { flex: none; }
</style>
</head>
<body>
  <main class="card">
    <div class="brand">
      <span class="brand-dot"></span>
      <span class="brand-name"><span>Pace with Us</span><span>Fitness</span></span>
    </div>

    <div class="disciplines">
      <div class="discipline swim" role="img" aria-label="Photo of a woman swimming"></div>
      <div class="discipline ride" role="img" aria-label="Photo of a woman cycling in a helmet"></div>
      <div class="discipline run" role="img" aria-label="Photo of a woman running"></div>
    </div>

    <div class="ribbon">
      <svg width="360" height="140" viewBox="0 0 360 140" aria-hidden="true">
        <polygon points="0,0 345,25 345,92 0,80" fill="var(--white)"/>
        <polygon points="0,80 345,92 360,140 0,122" fill="var(--ribbon-pale)"/>
        <line x1="0" y1="80" x2="345" y2="92" stroke="var(--teal)" stroke-width="3"/>
      </svg>
      <span class="person-name">Nina Carver</span>
      <span class="person-role">Business Director</span>
    </div>

    <ul class="contact">
      <li class="phone">0438 916 207
        <svg width="22" height="30" viewBox="0 0 22 30" aria-hidden="true"><rect x="2" y="2" width="18" height="26" rx="3" fill="none" stroke="var(--icon)" stroke-width="3"/><rect x="6" y="6" width="10" height="15" fill="var(--icon)"/></svg>
      </li>
      <li class="email">nina@pacewithusfitness.com.au
        <svg width="24" height="18" viewBox="0 0 24 18" aria-hidden="true"><rect x="1.5" y="1.5" width="21" height="15" fill="none" stroke="var(--icon)" stroke-width="2.5"/><polyline points="2,3 12,10 22,3" fill="none" stroke="var(--icon)" stroke-width="2.5"/></svg>
      </li>
      <li class="web">www.pacewithusfitness.com.au
        <svg width="22" height="22" viewBox="0 0 22 22" aria-hidden="true"><circle cx="11" cy="11" r="9" fill="none" stroke="var(--icon)" stroke-width="2.5"/><ellipse cx="11" cy="11" rx="4" ry="9" fill="none" stroke="var(--icon)" stroke-width="2"/><line x1="2" y1="11" x2="20" y2="11" stroke="var(--icon)" stroke-width="2"/></svg>
      </li>
    </ul>
  </main>
</body>
</html>
```